Verdant Holdings SA Business Cards

Dear all,
Thank you for reading my brief and project. My company is doing doing advisory in real estate and to comapnies + real estates services as asset management, brokerage, development etc.
I would like to get a business card for my company which is clear, professionnal and serious.
Please have a look to the attachement to see the logos of the company

Industry/Entity Type

Real Estate

Contact Information for Business Card

I would like to have in the business card the following
Principal side:
- Logo of the company (or Monogram)
- First and Last Name (Marcel Tobler)
- Mobile number
- email address

Second side:
- Address (Chemin des Vergers 17, 1292 Chambésy - Switzerland)
- website (www.verdantholdings.ch)

Requirements
Must have
• Refer to the typeface and logo colors

```html
<!DOCTYPE html>
<html lang="en">
<head>
<meta charset="utf-8">
<title>Verdant Holdings SA – Business Cards</title>
<link href="https://fonts.googleapis.com/css2?family=Montserrat:wght@400;500;600;700&display=swap" rel="stylesheet">
<style>
  :root {
    --backdrop: #dcdcd8;
    --card: #3e4b5c;
    --accent: #0b78c2;
    --ink-light: #ffffff;
    --shadow: rgba(30, 35, 45, 0.28);
  }
  * { box-sizing: border-box; margin: 0; padding: 0; }
  html, body {
    width: 1200px; height: 801px; overflow: hidden;
    background: var(--backdrop);
    font-family: "Montserrat", Arial, sans-serif;
  }
  .sheet {
    width: 1200px; height: 801px;
    display: flex; align-items: center; justify-content: center; gap: 40px;
  }
  .card {
    position: relative;
    width: 540px; height: 310px;
    background: var(--card);
    box-shadow: 0 10px 26px var(--shadow);
    color: var(--ink-light);
  }

  /* Front side */
  .brand-mark {
    position: absolute; left: 48px; top: 50%; transform: translateY(-50%);
    display: flex; align-items: center; gap: 12px;
  }
  .brand-mark__square { width: 22px; height: 22px; background: var(--ink-light); }
  .brand-mark__name {
    font-weight: 600; font-size: 17px; letter-spacing: 0.06em;
    text-transform: uppercase; color: var(--ink-light); line-height: 1.25;
  }
  .front__divider {
    position: absolute; left: 262px; top: 78px;
    width: 2px; height: 154px; background: var(--accent);
  }
  .contact {
    position: absolute; left: 290px; top: 78px;
  }
  .contact__name {
    color: var(--accent); font-weight: 700; font-size: 21px; line-height: 1.1;
  }
  .contact__role {
    font-size: 11.5px; font-weight: 500; margin-top: 5px; margin-bottom: 22px;
  }
  .contact__list { list-style: none; }
  .contact__item {
    display: flex; align-items: center; gap: 9px;
    font-size: 11px; font-weight: 500; margin-bottom: 8px; white-space: nowrap;
  }
  .contact__icon { width: 12px; height: 12px; flex: none; }

  /* Back side */
  .back__logo {
    position: absolute; left: 56px; top: 92px;
    display: flex; align-items: center; gap: 22px;
  }
  .back__square { width: 30px; height: 30px; background: var(--ink-light); }
  .back__divider { width: 2px; height: 96px; background: var(--ink-light); }
  .back__name {
    font-weight: 600; font-size: 26px; letter-spacing: 0.05em;
    text-transform: uppercase; color: var(--ink-light); line-height: 1.2;
  }
  .back__address {
    position: absolute; left: 0; right: 0; bottom: 48px;
    text-align: center; font-size: 12.5px; font-weight: 500; letter-spacing: 0.02em;
  }
</style>
</head>
<body>
<main class="sheet">

  <section class="card card--front" aria-label="Business card front">
    <div class="brand-mark">
      <span class="brand-mark__square"></span>
      <span class="brand-mark__name">Verdant<br>Holdings</span>
    </div>
    <span class="front__divider"></span>
    <div class="contact">
      <p class="contact__name">Marcel Tobler</p>
      <p class="contact__role">General Manager</p>
      <ul class="contact__list">
        <li class="contact__item">
          <svg class="contact__icon" viewBox="0 0 24 24" fill="#0b78c2" aria-hidden="true"><path d="M6.6 10.8a15.1 15.1 0 0 0 6.6 6.6l2.2-2.2c.3-.3.7-.4 1-.2 1.1.4 2.3.6 3.6.6.6 0 1 .4 1 1V20c0 .6-.4 1-1 1A17 17 0 0 1 3 4c0-.6.4-1 1-1h3.5c.6 0 1 .4 1 1 0 1.3.2 2.5.6 3.6.1.3 0 .7-.2 1z"/></svg>
          0412 558 903
        </li>
        <li class="contact__item">
          <svg class="contact__icon" viewBox="0 0 24 24" fill="#0b78c2" aria-hidden="true"><path d="M2 5h20v14H2z"/><path d="M2 5l10 8 10-8" fill="none" stroke="#3e4b5c" stroke-width="2"/></svg>
          m.tobler@verdantholdings.ch
        </li>
        <li class="contact__item">
          <svg class="contact__icon" viewBox="0 0 24 24" aria-hidden="true"><circle cx="12" cy="12" r="10" fill="#0b78c2"/><path d="M2 12h20M12 2c3 3 3 17 0 20M12 2c-3 3-3 17 0 20" fill="none" stroke="#3e4b5c" stroke-width="1.5"/></svg>
          www.verdantholdings.ch
        </li>
      </ul>
    </div>
  </section>

  <section class="card card--back" aria-label="Business card back">
    <div class="back__logo">
      <span class="back__square"></span>
      <span class="back__divider"></span>
      <span class="back__name">Verdant Holdings</span>
    </div>
    <p class="back__address">Chemin des Vergers 17, 1292 Chambésy - Switzerland</p>
  </section>

</main>
</body>
</html>
```